Consulting firm needs an infographic

The consulting we do needs a very graphic and understandable way to have perspective clients get exactly where we can help their company grow. I designed something that needs a lot of spice for it to look professional and relatable to them. This is being created to be used on a business card, as well as on posters, and social media.

```html
<!DOCTYPE html>
<html lang="en">
<head>
<meta charset="utf-8">
<title>Seeding Minds – What's Your Business?</title>
<link href="https://fonts.googleapis.com/css2?family=Open+Sans:wght@600;700;800&display=swap" rel="stylesheet">
<style>
  :root {
    --ink: #0d0d0d;
    --bg-light: #f7f9fa;
    --bg-dark: #bccbd5;
    --green-light: #f0f600;
    --green-dark: #3f8f1c;
    --orange-light: #ff8e45;
    --orange-dark: #c24a28;
    --yellow-light: #ffe500;
    --yellow-dark: #e3a000;
    --blue-light: #00e2ff;
    --blue-dark: #0873b3;
  }
  html, body {
    margin: 0;
    padding: 0;
    width: 1200px;
    height: 1200px;
    overflow: hidden;
  }
  .canvas {
    position: relative;
    width: 1200px;
    height: 1200px;
    background: radial-gradient(circle at 76% 40%, var(--bg-light) 0%, #e2e9ee 40%, var(--bg-dark) 100%);
    font-family: "Open Sans", Arial, sans-serif;
    color: var(--ink);
  }
  .brand-title {
    position: absolute;
    top: 72px;
    left: 0;
    width: 100%;
    margin: 0;
    text-align: center;
    font-size: 100px;
    font-weight: 800;
    letter-spacing: 2px;
    line-height: 1;
  }
  .brand-question {
    position: absolute;
    top: 199px;
    left: 0;
    width: 100%;
    margin: 0;
    text-align: center;
    font-size: 50px;
    font-weight: 700;
    line-height: 1;
  }
  .cycle-diagram {
    position: absolute;
    left: 0;
    top: 0;
    width: 1200px;
    height: 1200px;
  }
  .node-label {
    font-family: "Open Sans", Arial, sans-serif;
    font-weight: 700;
    fill: var(--ink);
    text-anchor: middle;
  }
  .node-title { font-size: 29px; font-weight: 700; }
  .node-sub { font-size: 18.5px; }
  .node-small { font-size: 16px; font-weight: 600; }
  .node-item { font-size: 19.5px; }
  .node-item-sm { font-size: 17px; }
</style>
</head>
<body>
<main class="canvas">
  <h1 class="brand-title">SEEDING MINDS</h1>
  <p class="brand-question">WHAT’S YOUR BUSINESS?</p>

  <svg class="cycle-diagram" viewBox="0 0 1200 1200" xmlns="http://www.w3.org/2000/svg">
    <defs>
      <linearGradient id="ring-green" x1="1" y1="0" x2="0" y2="1">
        <stop offset="0" stop-color="var(--green-light)"/>
        <stop offset="1" stop-color="var(--green-dark)"/>
      </linearGradient>
      <linearGradient id="ring-orange" x1="1" y1="0" x2="0" y2="1">
        <stop offset="0" stop-color="var(--orange-light)"/>
        <stop offset="1" stop-color="var(--orange-dark)"/>
      </linearGradient>
      <linearGradient id="ring-yellow" x1="1" y1="0" x2="0" y2="1">
        <stop offset="0" stop-color="var(--yellow-light)"/>
        <stop offset="1" stop-color="var(--yellow-dark)"/>
      </linearGradient>
      <linearGradient id="ring-blue" x1="1" y1="0" x2="0" y2="1">
        <stop offset="0" stop-color="var(--blue-light)"/>
        <stop offset="1" stop-color="var(--blue-dark)"/>
      </linearGradient>
      <linearGradient id="rim-white" x1="0" y1="0" x2="0" y2="1">
        <stop offset="0" stop-color="#ffffff"/>
        <stop offset="1" stop-color="#f2f2f2"/>
      </linearGradient>
      <linearGradient id="rim-grey" x1="0" y1="0" x2="0" y2="1">
        <stop offset="0" stop-color="#bdbdbd"/>
        <stop offset="1" stop-color="#f4f4f4"/>
      </linearGradient>
      <radialGradient id="disc-face" cx="0.45" cy="0.4" r="0.65">
        <stop offset="0" stop-color="#ffffff"/>
        <stop offset="0.6" stop-color="#f3f3f3"/>
        <stop offset="1" stop-color="#d9d9d9"/>
      </radialGradient>
      <filter id="drop" x="-30%" y="-30%" width="160%" height="160%">
        <feDropShadow dx="0" dy="10" stdDeviation="12" flood-color="#4a5a66" flood-opacity="0.35"/>
      </filter>
      <filter id="soft" x="-20%" y="-20%" width="140%" height="140%">
        <feDropShadow dx="0" dy="3" stdDeviation="5" flood-color="#000" flood-opacity="0.25"/>
      </filter>

      <linearGradient id="arrow-green" x1="1" y1="0" x2="0" y2="1">
        <stop offset="0" stop-color="#3aa521" stop-opacity="0"/>
        <stop offset="0.45" stop-color="#e8f51a"/>
        <stop offset="1" stop-color="#0f8a12"/>
      </linearGradient>
      <linearGradient id="arrow-blue" x1="1" y1="1" x2="0" y2="0">
        <stop offset="0" stop-color="#1a7fe0" stop-opacity="0"/>
        <stop offset="0.45" stop-color="#00e4ff"/>
        <stop offset="1" stop-color="#0c3fa8"/>
      </linearGradient>
      <linearGradient id="arrow-orange" x1="0" y1="0" x2="1" y2="0">
        <stop offset="0" stop-color="#ff8a1f" stop-opacity="0"/>
        <stop offset="0.35" stop-color="#ffb300"/>
        <stop offset="1" stop-color="#ff7a00"/>
      </linearGradient>
      <linearGradient id="arrow-red" x1="0" y1="0" x2="1" y2="0">
        <stop offset="0" stop-color="#ff2a2a" stop-opacity="0"/>
        <stop offset="0.35" stop-color="#ff6a3a"/>
        <stop offset="1" stop-color="#ff1818"/>
      </linearGradient>
    </defs>

    <!-- Flow arrows -->
    <g class="flow-arrow flow-arrow--to-vendors">
      <polygon fill="url(#arrow-green)"
        points="405,560 388,542 288,642 277,631 264,683 316,670 305,659" filter="url(#soft)"/>
    </g>
    <g class="flow-arrow flow-arrow--to-company">
      <polygon fill="url(#arrow-blue)"
        points="942,650 925,667 826,568 815,579 798,539 838,546 827,557" filter="url(#soft)"/>
    </g>
    <g class="flow-arrow flow-arrow--to-operations">
      <polygon fill="url(#arrow-orange)"
        points="394,987 468,987 468,975 502,997 468,1019 468,1007 394,1007"/>
    </g>
    <g class="flow-arrow flow-arrow--to-customers">
      <polygon fill="url(#arrow-red)"
        points="697,987 771,987 771,975 805,997 771,1019 771,1007 697,1007"/>
    </g>

    <!-- Your company node -->
    <g class="node node--company" transform="translate(596,460)">
      <circle r="164" fill="url(#ring-green)" filter="url(#drop)"/>
      <circle r="136" fill="url(#rim-white)" filter="url(#soft)"/>
      <circle r="128" fill="url(#rim-grey)"/>
      <circle r="120" fill="url(#disc-face)"/>
      <text class="node-label node-title" x="-4" y="-62">YOUR</text>
      <text class="node-label node-title" x="0" y="-35">COMPANY</text>
      <text class="node-label node-sub" x="0" y="-3">Product / Services</text>
      <text class="node-label node-small" x="0" y="37">Workforce</text>
      <text class="node-label node-small" x="0" y="55">Workforce</text>
      <text class="node-label node-small" x="0" y="73">Workforce</text>
    </g>

    <!-- Operations node -->
    <g class="node node--operations" transform="translate(596,834)">
      <circle r="164" fill="url(#ring-orange)" filter="url(#drop)"/>
      <circle r="136" fill="url(#rim-white)" filter="url(#soft)"/>
      <circle r="128" fill="url(#rim-grey)"/>
      <circle r="120" fill="url(#disc-face)"/>
      <text class="node-label node-item-sm" x="0" y="-54">EXECUTIVES</text>
      <g class="two-way-arrow" stroke="var(--ink)" stroke-width="1.6" fill="var(--ink)">
        <line x1="0" y1="-46" x2="0" y2="-27"/>
        <polygon points="-3,-42 3,-42 0,-48" stroke="none"/>
        <polygon points="-3,-31 3,-31 0,-25" stroke="none"/>
      </g>
      <text class="node-label node-item-sm" x="0" y="-7">ADMINISTRATIVE</text>
      <text class="node-label node-item-sm" x="0" y="38">PERSONNEL</text>
      <text class="node-label node-item-sm" x="0" y="66">LOGISTICS</text>
    </g>

    <!-- Vendors node -->
    <g class="node node--vendors" transform="translate(243,896)">
      <circle r="164" fill="url(#ring-yellow)" filter="url(#drop)"/>
      <circle r="136" fill="url(#rim-white)" filter="url(#soft)"/>
      <circle r="128" fill="url(#rim-grey)"/>
      <circle r="120" fill="url(#disc-face)"/>
      <text class="node-label node-item" x="0" y="-30">VENDORS</text>
      <text class="node-label node-item" x="0" y="7">RESOURCES</text>
      <text class="node-label node-item" x="0" y="44">COSTS</text>
    </g>

    <!-- Customers node -->
    <g class="node node--customers" transform="translate(947,894)">
      <circle r="164" fill="url(#ring-blue)" filter="url(#drop)"/>
      <circle r="136" fill="url(#rim-white)" filter="url(#soft)"/>
      <circle r="128" fill="url(#rim-grey)"/>
      <circle r="120" fill="url(#disc-face)"/>
      <text class="node-label node-item" x="3" y="-24">CUSTOMERS</text>
      <text class="node-label node-item" x="0" y="8">IDENTITY &amp; B&amp;M</text>
      <text class="node-label node-item" x="3" y="40">REVENUE</text>
    </g>
  </svg>
</main>
</body>
</html>
```